Book cover

I am working with my publisher to publish my book They came up with a book cover but I don't like it. I want to see different designs. The book Title is Shiftcraftery the subtitle How to Steer Upheaval with Focus, Poise & Resolve by Marilyn T. Hargreave
I want to use my Brand Colors including the blue. I am uploading the covers of my other book. This is a professional leadership book. The publisher will make the cover when providing them a new design. the Shiftcraftery one is one I played with on Canva. I would like more color and to incorporate the blue. I want a spot at the top where I can write a quote. Shiftcraftery is one word in the text so should be the same on the cover. I want the cover to show energy movement and am open to an image too. I am attaching logos for the feel of the brand and brand rgb codes.

```html
<!DOCTYPE html>
<html lang="en">
<head>
<meta charset="utf-8">
<title>Shiftcraftery — Book Cover</title>
<link href="https://fonts.googleapis.com/css2?family=Source+Sans+3:wght@300;400;600;700&display=swap" rel="stylesheet">
<style>
  :root {
    --teal-deep: #0a7d8c;
    --teal-mid: #1c8fa3;
    --teal-light: #6fb8c4;
    --coral: #e83a3a;
    --coral-soft: #f08a80;
    --paper: #f7f9f9;
    --white: #ffffff;
    --ink: #4a4545;
    --brand-teal: #15909c;
    --rule: #1d5f68;
  }
  html, body {
    margin: 0;
    padding: 0;
    overflow: hidden;
    background: var(--paper);
  }
  .cover {
    position: relative;
    width: 801px;
    height: 1200px;
    overflow: hidden;
    font-family: "Source Sans 3", sans-serif;
    background: var(--paper);
  }
  .cover-backdrop {
    position: absolute;
    inset: 0;
    width: 801px;
    height: 1200px;
  }
  .quote {
    position: absolute;
    top: 70px;
    left: 0;
    width: 801px;
    text-align: center;
    color: var(--white);
  }
  .quote-text {
    margin: 0;
    font-weight: 700;
    font-size: 25px;
    line-height: 34px;
  }
  .quote-source {
    display: inline-block;
    margin-top: 4px;
    padding: 0 24px 6px;
    font-weight: 300;
    font-size: 23px;
    border-bottom: 1px solid var(--rule);
  }
  .title {
    position: absolute;
    top: 448px;
    left: 0;
    width: 801px;
    margin: 0;
    text-align: center;
    white-space: nowrap;
    font-weight: 400;
    color: var(--white);
    font-size: 138px;
    line-height: 1;
    letter-spacing: -2px;
  }
  .subtitle {
    position: absolute;
    top: 722px;
    left: 90px;
    width: 621px;
    margin: 0;
    text-align: center;
    color: var(--ink);
    font-weight: 400;
    font-size: 50px;
    line-height: 64px;
  }
  .author {
    position: absolute;
    top: 1078px;
    left: 0;
    width: 801px;
    margin: 0;
    text-align: center;
    color: var(--brand-teal);
    font-weight: 700;
    font-size: 44px;
  }
</style>
</head>
<body>
<main class="cover">
  <svg class="cover-backdrop" viewBox="0 0 801 1200" aria-hidden="true">
    <defs>
      <linearGradient id="tealWash" x1="0" y1="0" x2="1" y2="1">
        <stop offset="0" stop-color="#58aebd"/>
        <stop offset="0.35" stop-color="#1a8ea2"/>
        <stop offset="0.7" stop-color="#0a7f8e"/>
        <stop offset="1" stop-color="#2f8f9b"/>
      </linearGradient>
      <filter id="softBlur" x="-30%" y="-30%" width="160%" height="160%">
        <feGaussianBlur stdDeviation="45"/>
      </filter>
      <filter id="edgeBlur" x="-10%" y="-10%" width="120%" height="120%">
        <feGaussianBlur stdDeviation="3"/>
      </filter>
      <linearGradient id="paperFade" x1="0" y1="0" x2="0" y2="1">
        <stop offset="0" stop-color="#f7f9f9" stop-opacity="0"/>
        <stop offset="0.35" stop-color="#f7f9f9" stop-opacity="1"/>
        <stop offset="1" stop-color="#fbfcfc"/>
      </linearGradient>
    </defs>
    <rect width="801" height="1200" fill="#f7f9f9"/>
    <ellipse cx="430" cy="640" rx="420" ry="140" fill="#f08a80" filter="url(#softBlur)"/>
    <ellipse cx="470" cy="600" rx="260" ry="90" fill="#e83a3a" filter="url(#softBlur)"/>
    <ellipse cx="720" cy="630" rx="140" ry="90" fill="#ec5a48" filter="url(#softBlur)"/>
    <rect x="0" y="700" width="801" height="500" fill="url(#paperFade)"/>
    <path d="M0 0 H801 V500 C700 520 620 480 520 505 C420 520 300 520 150 520 C70 520 40 480 0 410 Z"
          fill="url(#tealWash)" filter="url(#edgeBlur)"/>
    <ellipse cx="640" cy="520" rx="220" ry="60" fill="#7a6f70" opacity="0.55" filter="url(#softBlur)"/>
    <ellipse cx="120" cy="70" rx="200" ry="120" fill="#6fb8c4" opacity="0.45" filter="url(#softBlur)"/>
    <ellipse cx="760" cy="230" rx="90" ry="140" fill="#8bc3cc" opacity="0.4" filter="url(#softBlur)"/>
  </svg>

  <header class="quote">
    <p class="quote-text">“Shiftcraftery is the essential playbook<br>to turn uncertainty into possibility”</p>
    <span class="quote-source">Marilyn T. Hargreave</span>
  </header>

  <h1 class="title">Shiftcraftery</h1>

  <p class="subtitle">How to Steer Upheaval with Focus, Poise &amp; Resolve</p>

  <p class="author">Marilyn T. Hargreave</p>
</main>
</body>
</html>
```